Tobias Elvanor
Simple
Realtor
418 Paseo Lindero Blvd. Ste. 300
Danville, CA 94871
tobias@tobiaselvanor-example.com
www.tobiaselvanor-example.com
DRE Lic.# 02841937
Name of the company is Dunmore Ashby and I have my own personal logo.
Company Logo
Personal Logo
Company

```html
<!DOCTYPE html>
<html lang="en">
<head>
<meta charset="utf-8">
<title>Tobias Elvanor — Stationery Set</title>
<link href="https://fonts.googleapis.com/css2?family=Cormorant+Garamond:wght@500;600&family=Open+Sans:wght@400;600&display=swap" rel="stylesheet">
<style>
  :root{
    --red:#b3282d;
    --ink:#2b2b2b;
    --grey:#8a8a8a;
    --faint:#ececec;
    --paper:#ffffff;
    --ground:#e7e3de;
    --serif:"Cormorant Garamond", Georgia, serif;
    --sans:"Open Sans", Arial, sans-serif;
  }
  *{box-sizing:border-box;margin:0;padding:0}
  html,body{width:1200px;height:310px;overflow:hidden;background:var(--ground)}
  .canvas{position:relative;width:1200px;height:310px}
  .piece{position:absolute;background:var(--paper);box-shadow:0 2px 5px rgba(0,0,0,.25);overflow:hidden}
  .brand{display:flex;align-items:center;gap:5px;font-family:var(--serif);font-weight:600;color:var(--ink);letter-spacing:.06em;white-space:nowrap}
  .brand .mark{display:block;background:var(--red)}
  .brand-head{position:absolute;left:20px;top:10px;font-size:20px}
  .brand-head .mark{width:16px;height:16px}
  .tagline{position:absolute;left:62px;top:38px;font:400 6px var(--sans);color:var(--grey);letter-spacing:.1em}
  .small{font-family:var(--sans);color:var(--grey);line-height:1.35}

  /* business cards */
  .card{width:102px;height:58px}
  .card-logo{left:20px;top:125px;display:flex;align-items:center;justify-content:center}
  .card-logo .brand{font-size:9px}
  .card-logo .mark{width:8px;height:8px}
  .card-contact{left:132px;top:125px;padding:8px}
  .card-contact .brand{font-size:8px;color:var(--red)}
  .card-contact .mark{width:6px;height:6px}
  .card-contact .small{font-size:3.6px;margin-top:6px}
  .card-contact .rule{height:1px;background:var(--red);margin-top:4px}
  .card-square{left:20px;top:198px;display:flex;align-items:center;justify-content:center}
  .card-square .block{width:24px;height:24px;background:var(--ink)}
  .card-red{left:132px;top:198px;background:var(--red);display:flex;align-items:center;justify-content:center}
  .card-red .block{width:24px;height:24px;background:#fff}

  /* letterheads */
  .letter{width:175px;height:218px;top:46px}
  .letter-one{left:292px}
  .letter-two{left:497px}
  .letter .brand{position:absolute;left:58px;top:12px;font-size:8px}
  .letter .mark{width:7px;height:7px}
  .letter .head-contact{position:absolute;right:12px;top:10px;font-size:3.4px;text-align:right}
  .letter .watermark{position:absolute;left:50%;top:50%;width:62px;height:62px;margin:-31px 0 0 -31px;background:var(--faint)}
  .letter .watermark-name{position:absolute;left:0;right:0;top:148px;text-align:center;font:600 9px var(--serif);color:#e2e2e2;letter-spacing:.08em}
  .letter .footer{position:absolute;left:0;right:0;bottom:8px;text-align:center;font-size:3.4px}
  .letter .side-rule{position:absolute;right:0;top:0;width:3px;height:100%;background:var(--red)}

  /* DL envelopes */
  .dl{width:160px;height:72px;left:700px}
  .dl-one{top:112px}
  .dl-two{top:196px}
  .dl .brand{position:absolute;left:8px;top:7px;font-size:6.5px}
  .dl .mark{width:5px;height:5px}
  .dl .small{position:absolute;left:8px;top:18px;font-size:3.2px}
  .dl .rule{position:absolute;left:0;right:0;bottom:0;height:3px;background:var(--red)}

  /* flap envelopes */
  .flap-env{width:210px;height:86px;left:892px}
  .flap-env svg{position:absolute;left:0;top:0}
  .env-black{top:104px}
  .env-red{top:140px}
  .env-white{top:178px}
  .flap-env .center-mark{position:absolute;left:99px;top:42px;width:12px;height:12px;background:var(--red)}
</style>
</head>
<body>
<main class="canvas">

  <div class="brand brand-head"><span class="mark"></span>TOBIAS ELVANOR</div>
  <div class="tagline">REALTOR · DUNMORE ASHBY</div>

  <!-- business cards -->
  <section class="piece card card-logo"><div class="brand"><span class="mark"></span>TOBIAS ELVANOR</div></section>
  <section class="piece card card-contact">
    <div class="brand"><span class="mark"></span>TOBIAS ELVANOR</div>
    <div class="rule"></div>
    <p class="small">Realtor · DRE Lic.# 02841937<br>418 Paseo Lindero Blvd. Ste. 300, Danville, CA 94871<br>tobias@tobiaselvanor-example.com<br>www.tobiaselvanor-example.com</p>
  </section>
  <section class="piece card card-square"><span class="block"></span></section>
  <section class="piece card card-red"><span class="block"></span></section>

  <!-- letterheads -->
  <section class="piece letter letter-one">
    <div class="brand"><span class="mark"></span>TOBIAS ELVANOR</div>
    <p class="small head-contact">Office (925) 555-0142<br>tobias@tobiaselvanor-example.com<br>www.tobiaselvanor-example.com</p>
    <div class="watermark"></div>
    <p class="small footer">418 Paseo Lindero Blvd. Ste. 300 · Danville, CA 94871 · DRE Lic.# 02841937</p>
  </section>
  <section class="piece letter letter-two">
    <div class="brand"><span class="mark"></span>TOBIAS ELVANOR</div>
    <p class="small head-contact">Office (925) 555-0142<br>tobias@tobiaselvanor-example.com<br>www.tobiaselvanor-example.com</p>
    <div class="watermark"></div>
    <p class="small footer">418 Paseo Lindero Blvd. Ste. 300 · Danville, CA 94871 · DRE Lic.# 02841937</p>
    <div class="side-rule"></div>
  </section>

  <!-- DL envelopes -->
  <section class="piece dl dl-one">
    <div class="brand"><span class="mark"></span>TOBIAS ELVANOR</div>
    <p class="small">418 Paseo Lindero Blvd. Ste. 300<br>Danville, CA 94871</p>
    <div class="rule"></div>
  </section>
  <section class="piece dl dl-two">
    <div class="brand"><span class="mark"></span>TOBIAS ELVANOR</div>
    <p class="small">418 Paseo Lindero Blvd. Ste. 300<br>Danville, CA 94871</p>
    <div class="rule"></div>
  </section>

  <!-- flap envelopes -->
  <section class="piece flap-env env-black">
    <svg width="210" height="86" viewBox="0 0 210 86"><polygon points="0,0 210,0 105,50" fill="#2b2b2b"/></svg>
  </section>
  <section class="piece flap-env env-red">
    <svg width="210" height="86" viewBox="0 0 210 86"><polygon points="0,0 210,0 105,48" fill="#b3282d"/></svg>
  </section>
  <section class="piece flap-env env-white">
    <svg width="210" height="86" viewBox="0 0 210 86"><polyline points="0,0 105,48 210,0" fill="none" stroke="#cfcfcf" stroke-width="1"/></svg>
    <span class="center-mark"></span>
  </section>

</main>
</body>
</html>
```